Sassy, natural personal lubricant knows that it is not always about the packaging

An opportunity exists to create packaging for the world's first Macadamia Oil personal lubricant - Worrabee Silk. Unlike any other personal lubricants, this product is created from pure macadamia nut oil. The fatty acids naturally occurring in Macadamia oil are highly anti-inflammatory and are the closest in composition to human skin lipids. Using Worrabee Silk in such a vulnerable part of our bodies is the safest and gentlest way to enhance sexual enjoyment while moisturizing and adding lubrication. Worrabee Silk is completely free of the parabens, glycerins, fragrances, hormones, silicones and petroleum products known to irritate the delicate vaginal wall.

Design tone for Worrabee Silk:
- intelligent, but not condescending or patronizing
- elegant and dignified but not prudish
- clean, natural, uninhibited

Design specs:
- See attached file for packaging specs

Colors:
- refer to www.worrabee-example.com to see other products in the range. This is a guide only. Use of those colors is not mandatory.

Ingredients:

100% Macadamia Oil

Additional features:

- edible
- vegan
- gluten-free
- low allergen
- naturally anti-microbial and anti-inflammatory

See http://thebarebotanist-example.com/benefits-of-macadamia-nut-oil-in-skin-care/ for a list of the benefits of macadamia oil.

Target Market(s)

Our target market are the early adopters within the baby boomer set. Their age is a badge of honor, they are comfortable in their own skin and as sensual and fun-loving as ever. They are in their prime - still cool, still curious, still a little crazy. They are open to new possibilities, just as they have been at every age and stage. They still have plenty to do and plenty to enjoy. Being pre-menopausal or menopausal, natural lubrication may be diminishing. Worrabee Silk is the completely natural way to bring back the pleasure in sex.

Requirements
Must have
• Brandname: Worrabee Silk

Container Packaging specs: http://www.kelvorpackware-example.com/images/art/4871K07-C-FERN-RAISED.PDF
Dispenser: http://www.kelvorpackware-example.com/lotion-dispenser-pumps/p/kQT720R/
Should not have
• No post-coital pictures
No people
Nothing phallic

```html
<!DOCTYPE html>
<html lang="en">
<head>
<meta charset="utf-8">
<title>Worrabee Silk – Label Range</title>
<link rel="stylesheet" href="https://fonts.googleapis.com/css2?family=Cabin:wght@400;600&display=swap">
<style>
  :root {
    --backdrop: #e4e4e6;
    --label-white: #ffffff;
    --ink: #3b2f2f;
    --brand-ink: #8e3a7c;
    --lime: #c8d24a;
    --lime-soft: #e3e89a;
    --lime-deep: #a9b52c;
    --amber: #e39544;
    --amber-soft: #f1c59a;
    --amber-deep: #c9782c;
    --bronze-dark: #2b1a10;
    --bronze-light: #c89a5a;
    --berry-dark: #2a0d12;
    --berry-light: #d9788f;
  }
  * { margin: 0; padding: 0; box-sizing: border-box; }
  html, body { width: 840px; height: 1200px; overflow: hidden; }
  body {
    background: var(--backdrop);
    font-family: "Cabin", sans-serif;
    position: relative;
  }
  .label {
    position: absolute;
    top: 120px;
    width: 340px;
    height: 960px;
    background: var(--label-white);
    overflow: hidden;
  }
  .label--lime { left: 40px; --tone: var(--lime); --tone-soft: var(--lime-soft); --tone-deep: var(--lime-deep); --band-dark: var(--bronze-dark); --band-light: var(--bronze-light); }
  .label--amber { left: 460px; --tone: var(--amber); --tone-soft: var(--amber-soft); --tone-deep: var(--amber-deep); --band-dark: var(--berry-dark); --band-light: var(--berry-light); }

  .label__stripes { position: absolute; top: 40px; left: 0; width: 340px; height: 90px; }
  .label__stripes polygon { fill: var(--tone); }

  .label__mark {
    position: absolute; top: 165px; left: 50%;
    width: 34px; height: 34px; margin-left: -17px;
    border-radius: 50%;
    border: 3px solid var(--brand-ink);
  }
  .label__brand {
    position: absolute; top: 222px; left: 0; width: 100%;
    text-align: center;
    font-weight: 600;
    font-size: 44px;
    line-height: 46px;
    color: var(--brand-ink);
  }
  .label__descriptor {
    position: absolute; top: 352px; left: 0; width: 100%;
    text-align: center;
    font-weight: 400;
    font-size: 21px;
    line-height: 26px;
    color: var(--ink);
    z-index: 2;
  }
  .label__pattern {
    position: absolute; top: 300px; left: 0; width: 100%; height: 590px;
    background:
      radial-gradient(ellipse 70% 12% at 50% 14%, rgba(255,255,255,0.9), rgba(255,255,255,0) 70%),
      linear-gradient(to bottom, rgba(255,255,255,1) 0%, var(--tone-soft) 22%, var(--tone) 55%, var(--tone-deep) 100%);
  }
  .label__band {
    position: absolute; bottom: 34px; left: 0; width: 100%; height: 36px;
    background: linear-gradient(to right, var(--band-dark) 0%, var(--band-light) 45%, var(--band-light) 55%, var(--band-dark) 100%);
  }
</style>
</head>
<body>
  <section class="label label--lime">
    <svg class="label__stripes" viewBox="0 0 340 90" aria-hidden="true">
      <polygon points="0,20 340,0 340,22 130,30 0,42"/>
      <polygon points="0,56 200,44 340,34 340,62 0,74"/>
    </svg>
    <div class="label__pattern" role="img" aria-label="White floral lace pattern over a soft lime wash"></div>
    <span class="label__mark" aria-hidden="true"></span>
    <h1 class="label__brand">Worrabee<br>Silk</h1>
    <p class="label__descriptor">Personal lubricant<br>Pure Macadamia Oil</p>
    <div class="label__band"></div>
  </section>

  <section class="label label--amber">
    <svg class="label__stripes" viewBox="0 0 340 90" aria-hidden="true">
      <polygon points="0,20 340,0 340,22 130,30 0,42"/>
      <polygon points="0,56 200,44 340,34 340,62 0,74"/>
    </svg>
    <div class="label__pattern" role="img" aria-label="White floral lace pattern over a soft amber wash"></div>
    <span class="label__mark" aria-hidden="true"></span>
    <h1 class="label__brand">Worrabee<br>Silk</h1>
    <p class="label__descriptor">Personal lubricant<br>Pure Macadamia Oil</p>
    <div class="label__band"></div>
  </section>
</body>
</html>
```